K7 clearline

We are a glazing company specializing in frameless glass .
I would like the business cards in black with the logo taking up the most part of the front added with " frameless glass specialist's " below it.
On the back side I would like a list of what we do :
• shower screens
• glass balustrade / pool fencing
• mirrors
•office partitions
• sky lights
•shop fronts
•splash backs
Also include this information :
📧 - marcus@k7clearline.com
📞Marcus - 0412967528
📞 Colin - 0457 213 684
Updates
To all designs already posted can you include on the back of the card in the services part -
•splash backs
Target Market(s)
High end builders
Industry/Entity Type
Glazing
Contact Information for Business Card
On the back side I would like a list of what we do : • shower screens • glass balustrade / pool fencing • mirrors •office partitions • sky lights •shop fronts Also include this information : 📧 - marcus@k7clearline.com 📞Marcus - 0412967528 📞 Colin - 0457 213 684
Colors
Designer to choose colors to be used in the design.
Look and feel
Each slider illustrates characteristics of the customer's brand and the style your logo design should communicate.

```html
<!DOCTYPE html>
<html lang="en">
<head>
<meta charset="utf-8">
<title>K7 Clearline – Business Cards</title>
<link href="https://fonts.googleapis.com/css2?family=Montserrat:wght@600;700&family=Lato:wght@400;700&display=swap" rel="stylesheet">
<style>
  :root {
    --bg: #2a2a2b;
    --card-dark: #121212;
    --teal: #3cc4a8;
    --teal-bright: #10b9b8;
    --white: #ffffff;
    --muted: #d9d9d9;
  }
  * { box-sizing: border-box; margin: 0; padding: 0; }
  html, body { width: 1200px; height: 875px; overflow: hidden; }
  body {
    background: var(--bg);
    position: relative;
    font-family: 'Lato', sans-serif;
  }
  .card {
    position: absolute;
    width: 580px;
    height: 330px;
    border-radius: 22px;
    background: var(--card-dark);
    box-shadow: 0 20px 40px rgba(0,0,0,.45);
  }
  .brand {
    position: absolute;
    font-family: 'Montserrat', sans-serif;
    font-weight: 700;
    text-transform: uppercase;
    line-height: .9;
    color: var(--teal);
  }
  .brand-code { display: block; font-size: 118px; letter-spacing: -2px; }
  .brand-word { display: block; font-size: 34px; letter-spacing: 3px; margin-top: 6px; }

  /* Front card */
  .card-front { left: 70px; top: 80px; }
  .card-front .brand { left: 48px; top: 74px; }
  .brand-tagline {
    display: block;
    margin-top: 12px;
    font-family: 'Montserrat', sans-serif;
    font-weight: 600;
    font-size: 11.5px;
    letter-spacing: 1.6px;
    color: var(--white);
  }
  .divider-front {
    position: absolute;
    left: 318px; top: 88px;
    width: 2px; height: 150px;
    background: var(--teal);
  }
  .services {
    position: absolute;
    left: 346px; top: 74px;
    list-style: none;
    color: var(--white);
    font-size: 17px;
    line-height: 22px;
  }
  .services li { display: flex; align-items: center; gap: 12px; }
  .services li::before {
    content: "";
    width: 10px; height: 10px;
    background: var(--teal);
    flex: none;
  }

  /* Back card */
  .card-back { left: 550px; top: 465px; }
  .card-back .brand { right: 38px; top: 36px; text-align: right; }
  .card-back .brand-code { font-size: 84px; }
  .card-back .brand-word { font-size: 24px; letter-spacing: 2px; }
  .contacts {
    position: absolute;
    left: 38px; bottom: 38px;
    display: flex;
    align-items: flex-end;
    gap: 26px;
  }
  .contact-name {
    font-family: 'Montserrat', sans-serif;
    font-weight: 700;
    font-size: 38px;
    color: var(--teal);
    text-transform: uppercase;
    line-height: 1;
    margin-bottom: 6px;
  }
  .contact-line {
    display: flex;
    align-items: center;
    gap: 8px;
    color: var(--white);
  }
  .contact-phone { font-size: 22px; font-weight: 700; }
  .contact-email { font-size: 14px; margin-top: 4px; }
  .contact-line svg { width: 14px; height: 14px; flex: none; }
  .divider-back {
    width: 2px; height: 92px;
    background: var(--teal);
  }
</style>
</head>
<body>

<section class="card card-front">
  <div class="brand">
    <span class="brand-code">K7</span>
    <span class="brand-word">Clearline</span>
    <span class="brand-tagline">Frameless Glass Specialists</span>
  </div>
  <div class="divider-front"></div>
  <ul class="services">
    <li>Shower Screens</li>
    <li>Glass Balustrade</li>
    <li>Pool Fencing</li>
    <li>Mirrors</li>
    <li>Office Partitions</li>
    <li>Sky Lights</li>
    <li>Shop Fronts</li>
    <li>Splash Backs</li>
  </ul>
</section>

<section class="card card-back">
  <div class="brand"><span class="brand-code">K7</span><span class="brand-word">Clearline</span></div>
  <div class="contacts">
    <div class="contact">
      <p class="contact-name">Marcus</p>
      <p class="contact-line contact-phone">
        <svg viewBox="0 0 24 24"><path fill="#3cc4a8" d="M6.6 10.8a15.1 15.1 0 0 0 6.6 6.6l2.2-2.2c.3-.3.7-.4 1-.2 1.1.4 2.3.6 3.6.6.6 0 1 .4 1 1V20c0 .6-.4 1-1 1A17 17 0 0 1 3 4c0-.6.4-1 1-1h3.5c.6 0 1 .4 1 1 0 1.3.2 2.5.6 3.6.1.3 0 .7-.2 1z"/></svg>
        0412 967 528
      </p>
      <p class="contact-line contact-email">
        <svg viewBox="0 0 24 24"><path fill="#3cc4a8" d="M2 5h20v14H2z"/><path fill="none" stroke="#121212" stroke-width="2" d="M2 5l10 8 10-8"/></svg>
        marcus@k7clearline.com
      </p>
    </div>
    <div class="divider-back"></div>
    <div class="contact">
      <p class="contact-name">Colin</p>
      <p class="contact-line contact-phone">
        <svg viewBox="0 0 24 24"><path fill="#3cc4a8" d="M6.6 10.8a15.1 15.1 0 0 0 6.6 6.6l2.2-2.2c.3-.3.7-.4 1-.2 1.1.4 2.3.6 3.6.6.6 0 1 .4 1 1V20c0 .6-.4 1-1 1A17 17 0 0 1 3 4c0-.6.4-1 1-1h3.5c.6 0 1 .4 1 1 0 1.3.2 2.5.6 3.6.1.3 0 .7-.2 1z"/></svg>
        0457 213 684
      </p>
      <p class="contact-line contact-email">
        <svg viewBox="0 0 24 24"><path fill="#3cc4a8" d="M2 5h20v14H2z"/><path fill="none" stroke="#121212" stroke-width="2" d="M2 5l10 8 10-8"/></svg>
        colin@k7clearline.com
      </p>
    </div>
  </div>
</section>

</body>
</html>
```